update company powerpoint deck - inject more power/personality into the deck

We would like a designer to provide us with a powerpoint template based on our brand guidelines. Current brand guidelines, colours and existing deck provided.
Current deck lacks punch. We really like our black and white elements - but need options for graphs, tables and charts. We potentially need more supplementary colours to what is currently in our brand guidelines.

Target Market(s)

listed companies - B2B. We are a management consulting company.

Industry/Entity Type

Consulting

Font styles to use
Serif
Sans Serif

Requirements
Must have
• Slides that are common for consulting companies.
The ability to use the deck as a report - not just a presentation format

```html
<!DOCTYPE html>
<html lang="en">
<head>
<meta charset="utf-8">
<title>Northgate Advisory – Dashboard Slides</title>
<link rel="stylesheet" href="https://fonts.googleapis.com/css2?family=Open+Sans:wght@400;600;700;800&family=Roboto:wght@300;400;500;700&display=swap">
<style>
  :root{
    --ink:#2e2e3d;
    --teal:#5ab5c0;
    --teal-dark:#1f5d64;
    --teal-pale:#a9dce1;
    --card:#f1f1f1;
    --card-mid:#dcdcdc;
    --track:#ffffff;
    --grey-card:#cacaca;
    --navy:#1f3b57;
    --green:#5fc0a0;
    --icon-deep:#4f8a80;
    --icon-soft:#8fb3bd;
    --icon-blue:#2f7fc1;
    --cost:#3a93b8;
    --revenue:#80a7e8;
    --alert:#c00000;
    --muted:#6b6b6b;
    --band:#f6f6f6;
  }
  *{margin:0;padding:0;box-sizing:border-box}
  html,body{width:1200px;height:1000px;overflow:hidden;background:#fff}
  body{position:relative;font-family:"Roboto",Arial,sans-serif;color:var(--ink)}
  .slide{position:absolute;background:#fff;box-shadow:0 2px 8px rgba(0,0,0,.18)}
  .slide--kpi{left:113px;top:25px;width:914px;height:528px}
  .slide--ops{left:266px;top:555px;width:668px;height:375px}
  .abs{position:absolute}
  .card{position:absolute;background:var(--card)}
  .card--mid{background:var(--card-mid)}
  .card--grey{background:var(--grey-card)}
  .heading{font-family:"Open Sans",Arial,sans-serif;font-weight:700;font-size:13.5px;color:var(--ink);letter-spacing:.2px}
  .more{font-family:"Open Sans",Arial,sans-serif;font-size:15px;color:var(--ink);letter-spacing:.5px}
  .more::after{content:"";display:inline-block;margin-left:8px;vertical-align:3px;border-left:4px solid transparent;border-right:4px solid transparent;border-top:6px solid #666}
  .figure{font-family:"Open Sans",Arial,sans-serif;font-weight:700;font-size:31px;color:var(--ink)}
  .figure sup{font-size:18px;vertical-align:11px;margin-right:1px}
  .label{font-size:12.5px;color:var(--ink)}
  .delta{font-size:14px;color:var(--teal)}
  .cta{position:absolute;background:var(--teal);color:#fff;border-radius:17px;font-size:14.5px;text-align:center;line-height:36px;letter-spacing:.2px}
  .bar{position:absolute;height:6px;background:#fff;border-radius:3px}
  .bar__fill{height:100%;background:var(--teal);border-radius:3px}
  .pct{font-size:12px;color:var(--teal)}
  .ring-text{position:absolute;width:120px;text-align:center}
  .ring-text .figure{font-size:30px;line-height:1.1}
  .ring-caption{font-size:11px;line-height:1.2;margin-top:9px}
  .footer-note{font-size:6.5px;color:#444}
  .brand-name{font-family:"Roboto",Arial,sans-serif;font-weight:400;font-size:7.5px;color:#333}
  .page-num{font-size:8px;color:#333;margin-left:14px}
  .band{position:absolute;background:var(--band)}
  svg{position:absolute;overflow:visible}
  .ops-title{font-family:"Open Sans",Arial,sans-serif;font-weight:700;font-size:7.2px;color:var(--navy)}
  .ops-title--muted{color:var(--muted)}
  .ops-title--alert{color:var(--alert)}
  .ops-value{font-family:"Open Sans",Arial,sans-serif;font-weight:700;font-size:20px;color:var(--navy);line-height:1}
  .ops-value--green{color:var(--green)}
  .review-box{position:absolute;background:#eeeeee;border-radius:8px;text-align:center;font-size:7px;color:#333;line-height:1.2}
  .review-box b{display:block;font-family:"Open Sans",Arial,sans-serif;font-size:20px;color:#6e9bab;font-weight:600;line-height:1.1;margin-top:8px}
  .legend{font-family:"Open Sans",Arial,sans-serif;font-weight:700;font-size:14px;color:var(--navy)}
  .legend i{display:inline-block;width:9px;height:9px;margin-right:6px;vertical-align:1px}
</style>
</head>
<body>

<!-- Slide 41: KPI dashboard -->
<section class="slide slide--kpi"></section>
<div class="band" role="img" aria-label="Light dotted footer pattern band" style="left:133px;top:517px;width:882px;height:33px"></div>

<div class="card" style="left:163px;top:57px;width:211px;height:254px"></div>
<div class="abs figure" style="left:194px;top:68px"><sup>$</sup>6,00,000</div>
<div class="abs label" style="left:195px;top:111px">Management Consulting</div>
<div class="abs delta" style="left:194px;top:136px">+3.4%</div>
<div class="cta" style="left:186px;top:168px;width:165px;height:32px">ADD FOUND</div>
<div class="abs label" style="left:194px;top:218px">Your Text Here</div>
<div class="bar" style="left:186px;top:237px;width:102px"><div class="bar__fill" style="width:81%"></div></div>
<div class="abs label" style="left:194px;top:264px">Your Text Here</div>
<div class="bar" style="left:186px;top:283px;width:102px"><div class="bar__fill" style="width:47%"></div></div>

<div class="card" style="left:390px;top:57px;width:348px;height:254px"></div>
<div class="abs more" style="left:659px;top:72px">MORE</div>
<svg class="line-chart" style="left:390px;top:57px" width="348" height="254" viewBox="390 57 348 254" font-family="Roboto, Arial, sans-serif" font-size="8" fill="#555">
  <g stroke="#d6d6d6" stroke-width="1">
    <line x1="449" y1="112" x2="700" y2="112"/><line x1="449" y1="130" x2="700" y2="130"/>
    <line x1="449" y1="148" x2="700" y2="148"/><line x1="449" y1="166" x2="700" y2="166"/>
    <line x1="449" y1="184" x2="700" y2="184"/><line x1="449" y1="201" x2="700" y2="201"/>
    <line x1="449" y1="219" x2="700" y2="219"/><line x1="449" y1="237" x2="700" y2="237"/>
    <line x1="449" y1="255" x2="700" y2="255" stroke="#999"/>
  </g>
  <g text-anchor="end">
    <text x="443" y="115">$40,000</text><text x="443" y="133">$35,000</text>
    <text x="443" y="151">$30,000</text><text x="443" y="169">$25,000</text>
    <text x="443" y="187">$20,000</text><text x="443" y="204">$15,000</text>
    <text x="443" y="222">$10,000</text><text x="443" y="240">$5,000</text>
    <text x="443" y="258">$0</text>
  </g>
  <g text-anchor="middle">
    <text x="449" y="269">2015</text><text x="485" y="269">2016</text>
    <text x="520" y="269">2017</text><text x="556" y="269">2018</text>
    <text x="592" y="269">2019</text><text x="628" y="269">2020</text>
    <text x="664" y="269">2021</text><text x="700" y="269">2022</text>
  </g>
  <path d="M485,237 C500,215 508,193 520,193 C535,193 543,212 556,210 C570,208 578,150 592,150 C606,150 613,176 628,175 C643,174 652,140 664,120" fill="none" stroke="var(--teal)" stroke-width="4" stroke-linecap="round"/>
  <path d="M485,255 C497,240 508,222 520,222 C535,222 543,232 556,229 C572,226 578,150 592,150 C607,150 615,195 628,195 C642,195 654,160 664,147" fill="none" stroke="var(--teal-dark)" stroke-width="4" stroke-linecap="round"/>
  <rect x="572" y="110" width="44" height="24" rx="4" fill="var(--teal-pale)"/>
  <text x="594" y="129" text-anchor="middle" font-size="9" fill="#333">Your</text>
  <text x="594" y="141" text-anchor="middle" font-size="9" fill="#333">Text</text>
  <circle cx="597" cy="151" r="4" fill="var(--teal-dark)" stroke="#fff" stroke-width="1.5"/>
  <line x1="498" y1="284" x2="518" y2="284" stroke="var(--teal-dark)" stroke-width="3"/>
  <text x="521" y="287">Your Text 1</text>
  <line x1="569" y1="284" x2="589" y2="284" stroke="var(--teal)" stroke-width="3"/>
  <text x="592" y="287">Your Text 2</text>
</svg>

<div class="card" style="left:754px;top:57px;width:212px;height:254px"></div>
<div class="abs heading" style="left:775px;top:74px">YOUR TITLE HERE</div>
<svg class="ring" style="left:789px;top:115px" width="140" height="140" viewBox="-70 -70 140 140">
  <circle r="63" fill="none" stroke="var(--track)" stroke-width="13"/>
  <circle r="63" fill="none" stroke="var(--teal)" stroke-width="13" stroke-linecap="round" pathLength="100" stroke-dasharray="54 100" transform="scale(-1 1) rotate(-90)"/>
</svg>
<div class="ring-text" style="left:799px;top:142px">
  <div class="figure">54%</div>
  <div class="ring-caption">Green<br>marketing is a<br>practice</div>
</div>
<div class="abs" style="left:764px;top:265px;width:192px;text-align:center;font-size:12px;line-height:1.2">Green marketing is a practice whereby companies seek</div>

<div class="card" style="left:163px;top:328px;width:282px;height:189px"></div>
<div class="abs heading" style="left:194px;top:344px">YOUR TITLE HERE</div>
<div class="abs label" style="left:194px;top:397px">Your Text Here</div>
<div class="abs pct" style="left:395px;top:397px">80%</div>
<div class="bar" style="left:186px;top:415px;width:238px"><div class="bar__fill" style="width:80%"></div></div>
<div class="abs label" style="left:194px;top:461px">Your Text Here</div>
<div class="abs pct" style="left:395px;top:461px">50%</div>
<div class="bar" style="left:186px;top:480px;width:238px"><div class="bar__fill" style="width:47%"></div></div>

<div class="card" style="left:462px;top:328px;width:165px;height:189px"></div>
<div class="card card--mid" style="left:627px;top:328px;width:174px;height:189px"></div>
<div class="card" style="left:801px;top:328px;width:165px;height:189px"></div>
<div class="abs heading" style="left:486px;top:344px">YOUR TITLE</div>
<div class="abs more" style="left:897px;top:344px;font-size:14px">MORE</div>

<svg class="ring" style="left:474px;top:368px" width="140" height="140" viewBox="-70 -70 140 140">
  <circle r="63" fill="none" stroke="var(--track)" stroke-width="12"/>
  <circle r="63" fill="none" stroke="var(--teal)" stroke-width="12" stroke-linecap="round" pathLength="100" stroke-dasharray="70 100" transform="scale(-1 1) rotate(-90)"/>
</svg>
<div class="ring-text" style="left:484px;top:404px">
  <div class="figure">70%</div>
  <div class="ring-caption" style="margin-top:7px">Risk<br>Management</div>
</div>

<svg class="ring" style="left:643px;top:368px" width="140" height="140" viewBox="-70 -70 140 140">
  <circle r="63" fill="none" stroke="var(--track)" stroke-width="12"/>
  <circle r="63" fill="none" stroke="var(--teal)" stroke-width="12" stroke-linecap="round" pathLength="100" stroke-dasharray="54 100" transform="scale(-1 1) rotate(-90)"/>
</svg>
<div class="ring-text" style="left:653px;top:404px">
  <div class="figure">54%</div>
  <div class="ring-caption" style="margin-top:7px">Project<br>Management<br>Office</div>
</div>

<svg class="ring" style="left:813px;top:368px" width="140" height="140" viewBox="-70 -70 140 140">
  <circle r="63" fill="none" stroke="var(--track)" stroke-width="12"/>
  <circle r="63" fill="none" stroke="var(--teal)" stroke-width="12" stroke-linecap="round" pathLength="100" stroke-dasharray="30 100" transform="scale(-1 1) rotate(-90)"/>
</svg>
<div class="ring-text" style="left:823px;top:404px">
  <div class="figure">30%</div>
  <div class="ring-caption" style="margin-top:7px">Monitoring<br>and Evaluation<br>Team</div>
</div>

<div class="abs footer-note" style="left:133px;top:525px">Northgate Advisory 2020 Confidential</div>
<div class="abs" style="left:920px;top:524px;white-space:nowrap"><span class="brand-name">Northgate Advisory</span><span class="page-num">41</span></div>

<!-- Slide 40: consulting operations dashboard -->
<section class="slide slide--ops"></section>
<div class="band" role="img" aria-label="Light dotted footer pattern band" style="left:282px;top:898px;width:636px;height:26px"></div>

<div class="card card--grey" style="left:321px;top:578px;width:179px;height:52px"></div>
<div class="card card--grey" style="left:510px;top:578px;width:179px;height:52px"></div>
<div class="card card--grey" style="left:699px;top:578px;width:179px;height:52px"></div>
<div class="card card--grey" style="left:321px;top:640px;width:368px;height:123px"></div>
<div class="card card--grey" style="left:699px;top:640px;width:179px;height:123px"></div>
<div class="card card--grey" style="left:321px;top:773px;width:179px;height:119px"></div>
<div class="card card--grey" style="left:510px;top:773px;width:179px;height:119px"></div>
<div class="card card--grey" style="left:699px;top:773px;width:179px;height:119px"></div>

<svg class="icons" style="left:0;top:0" width="1200" height="1000" viewBox="0 0 1200 1000" fill="none" stroke="#fff" stroke-width="1.2">
  <circle cx="348" cy="604" r="14" fill="var(--icon-deep)" stroke="none"/>
  <path d="M341,611 h14 M342,610 v-5 M346,610 v-8 M350,610 v-6 M354,610 v-10"/>
  <circle cx="537" cy="604" r="14" fill="var(--icon-deep)" stroke="none"/>
  <path d="M530,611 h14 M531,610 v-4 M535,610 v-7 M539,610 v-5 M543,610 v-10 M540,600 l3,-2 l1,3"/>
  <circle cx="726" cy="604" r="14" fill="var(--green)" stroke="none"/>
  <rect x="720" y="597" width="10" height="13" rx="1"/><circle cx="731" cy="607" r="3"/>
  <circle cx="344" cy="662" r="11" fill="var(--icon-soft)" stroke="none"/>
  <rect x="340" y="656" width="8" height="11" rx="1"/><path d="M342,660 h4 M342,663 h4"/>
  <circle cx="721" cy="662" r="11" fill="var(--icon-soft)" stroke="none"/>
  <circle cx="721" cy="662" r="5"/><circle cx="721" cy="662" r="2"/>
  <circle cx="344" cy="796" r="12" fill="var(--icon-blue)" stroke="none"/>
  <rect x="340" y="790" width="8" height="12" rx="1"/><path d="M342,794 h4 M342,797 h4"/>
  <circle cx="533" cy="796" r="12" fill="var(--icon-blue)" stroke="none"/>
  <rect x="529" y="790" width="8" height="12" rx="1"/><path d="M531,794 h4 M531,797 h4"/>
  <circle cx="722" cy="796" r="12" fill="var(--icon-blue)" stroke="none"/>
  <rect x="718" y="790" width="8" height="12" rx="1"/><path d="M720,794 h4 M720,797 h4"/>
</svg>

<div class="abs ops-title" style="left:375px;top:589px">AMOUNT OF CONSULTATION</div>
<div class="abs ops-value" style="left:375px;top:602px">73</div>
<div class="abs ops-title" style="left:564px;top:589px">REVENUE THE NEXT 12 MONTHS</div>
<div class="abs ops-value" style="left:564px;top:602px">$13,920</div>
<div class="abs ops-title" style="left:753px;top:589px">COST THE NEXT 12 MONTHS</div>
<div class="abs ops-value ops-value--green" style="left:753px;top:602px">$35,750</div>

<div class="abs ops-title ops-title--muted" style="left:366px;top:657px">SUM OF COSTS AND REVENUES</div>
<svg class="bar-chart" style="left:321px;top:640px" width="368" height="123" viewBox="321 640 368 123" font-family="Open Sans, Arial, sans-serif" font-weight="700">
  <g fill="var(--navy)" font-size="13">
    <text x="350" y="696">5…</text><text x="350" y="722">3…</text><text x="350" y="748">1…</text>
  </g>
  <rect x="374" y="683" width="89" height="15" fill="var(--cost)"/>
  <rect x="463" y="683" width="46" height="15" fill="var(--revenue)" stroke="#5f86c8" stroke-width=".6"/>
  <rect x="374" y="709" width="64" height="15" fill="var(--cost)"/>
  <rect x="438" y="709" width="111" height="15" fill="var(--revenue)" stroke="#5f86c8" stroke-width=".6"/>
  <rect x="374" y="735" width="109" height="15" fill="var(--cost)"/>
  <rect x="483" y="735" width="61" height="15" fill="var(--revenue)" stroke="#5f86c8" stroke-width=".6"/>
  <g fill="#fff" font-size="13" text-anchor="middle">
    <text x="418" y="696">3.5</text><text x="486" y="696">1.8</text>
    <text x="406" y="722">2.5</text><text x="493" y="722">4.4</text>
    <text x="428" y="748">4.3</text><text x="513" y="748">2.4</text>
  </g>
</svg>
<div class="abs legend" style="left:594px;top:695px"><i style="background:var(--cost)"></i>COST</div>
<div class="abs legend" style="left:594px;top:719px"><i style="background:var(--revenue)"></i>REVENUE</div>

<div class="abs ops-title ops-title--muted" style="left:745px;top:657px">CONSULTING TO REVIEW</div>
<div class="review-box" style="left:715px;top:688px;width:69px;height:63px"><b>7</b>Consulting<br>For Finance</div>
<div class="review-box" style="left:797px;top:688px;width:69px;height:63px"><b>9</b>Consulting for<br>Project<br>Management</div>

<div class="abs ops-title ops-title--alert" style="left:366px;top:790px">CONTRACTS PER STATUS</div>
<div class="abs ops-title ops-title--alert" style="left:555px;top:790px">CONTRACTS PER CATEGORY</div>
<div class="abs ops-title ops-title--alert" style="left:745px;top:790px">CONTRACTS PER ORG. UNIT</div>

<svg class="donuts" style="left:0;top:0" width="1200" height="1000" viewBox="0 0 1200 1000" font-family="Roboto, Arial, sans-serif" font-size="6.5" fill="#555">
  <g transform="translate(409 849) rotate(-90)" fill="none" stroke-width="6">
    <circle r="22" stroke="#3a93b8" pathLength="100" stroke-dasharray="51 49"/>
    <circle r="22" stroke="#5fb9c1" pathLength="100" stroke-dasharray="27 73" stroke-dashoffset="-51"/>
    <circle r="22" stroke="#7fb8d8" pathLength="100" stroke-dasharray="12 88" stroke-dashoffset="-78"/>
    <circle r="22" stroke="#a6cfd5" pathLength="100" stroke-dasharray="10 90" stroke-dashoffset="-90"/>
  </g>
  <text x="409" y="847" text-anchor="middle" font-size="9" font-weight="700" fill="#333">39</text>
  <text x="409" y="858" text-anchor="middle" font-size="7" fill="#333">Contracts</text>
  <text x="439" y="848">Project 1</text><text x="446" y="856">51%</text>
  <text x="359" y="871">Project 2</text><text x="363" y="879">27%</text>
  <text x="349" y="844">Project 3</text><text x="355" y="852">12%</text>
  <text x="358" y="817">Project 4</text><text x="365" y="825">10%</text>

  <g transform="translate(598 849) rotate(-90)" fill="none" stroke-width="4">
    <circle r="24" stroke="#3a93b8" pathLength="100" stroke-dasharray="43 57"/>
    <circle r="24" stroke="#5fb9c1" pathLength="100" stroke-dasharray="23 77" stroke-dashoffset="-43"/>
    <circle r="24" stroke="#7fb8d8" pathLength="100" stroke-dasharray="10 90" stroke-dashoffset="-66"/>
    <circle r="24" stroke="#a6cfd5" pathLength="100" stroke-dasharray="13 87" stroke-dashoffset="-76"/>
    <circle r="24" stroke="#c4dfe3" pathLength="100" stroke-dasharray="11 89" stroke-dashoffset="-89"/>
  </g>
  <text x="637" y="838">Project 1</text><text x="644" y="846">43%</text>
  <text x="547" y="833">Project</text><text x="552" y="841">4…</text>
  <text x="571" y="818">Project 5…</text>
  <text x="540" y="853">Project 3</text><text x="547" y="861">10%</text>
  <text x="545" y="870">Project 2</text><text x="552" y="878">23%</text>

  <g transform="translate(787 849) rotate(-90)" fill="none" stroke-width="4">
    <circle r="22" stroke="#3a93b8" pathLength="100" stroke-dasharray="36 64"/>
    <circle r="22" stroke="#5fb9c1" pathLength="100" stroke-dasharray="19 81" stroke-dashoffset="-36"/>
    <circle r="22" stroke="#7fb8d8" pathLength="100" stroke-dasharray="8 92" stroke-dashoffset="-55"/>
    <circle r="22" stroke="#a6cfd5" pathLength="100" stroke-dasharray="7 93" stroke-dashoffset="-63"/>
    <circle r="22" stroke="#c4dfe3" pathLength="100" stroke-dasharray="12 88" stroke-dashoffset="-70"/>
    <circle r="22" stroke="#2f7fc1" pathLength="100" stroke-dasharray="18 82" stroke-dashoffset="-82"/>
  </g>
  <text x="787" y="847" text-anchor="middle" font-size="9" font-weight="700" fill="#333">17</text>
  <text x="787" y="858" text-anchor="middle" font-size="7" fill="#333">Contracts</text>
  <text x="818" y="828">Project 1</text><text x="823" y="836">36%</text>
  <text x="816" y="871">Project 2</text><text x="821" y="879">19%</text>
  <text x="747" y="875">Project 3</text><text x="756" y="883">8%</text>
  <text x="733" y="857">Project 4</text><text x="741" y="865">7%</text>
  <text x="721" y="837">Project 5</text><text x="726" y="845">12%</text>
  <text x="752" y="826">Project 6</text><text x="759" y="833">18%</text>
</svg>

<div class="abs footer-note" style="left:290px;top:910px;font-size:5.5px">Northgate Advisory 2020 Confidential</div>
<div class="abs" style="left:848px;top:908px;white-space:nowrap"><span class="brand-name" style="font-size:6.5px">Northgate Advisory</span><span class="page-num" style="font-size:7px;margin-left:10px">40</span></div>

</body>
</html>
```